依頼詳細
起業をしようと思っているが
具体的にはどのようにしていいのかわからない方向けに
比較的安価でセミナーを開催しようと考えています。

希望しては、信頼感とフレンドリーさを感じられるサイトデザインを
提案していただければ幸いです。

参考として他社で気に入っているサイトは下記になります。
http://www.kirameki-kaigi.example/kaiin/yuutai.html?ref=QWpTzKe3nd8RHsVuLmAxYPbEOF

また文章部分については自分でも考えますので
「******」などの伏せ字にしていただいても結構です。

たたき台として案をエクセルファイルにまとめまてあります。
必ずしもエクセルにある文章通りにしたりする必要はなく
構成を変えていただいたり、キャッチコピーを変えるなど
むしろしていただければ幸いです。
文章や構成などをうまく編集していただいた方には
万が一、当選しなくても、別に参加賞などで対応させていただきます。

今回はデザインのみでコーディングは不要です。
皆様、
非常に素晴らしい力作をご提案いただきありがとうございます。

まだ
提案予約をしていただいていますが
提出ができていない方がいらっしゃるため
期限を少し伸ばしたいと思います。

引き続きすばらしい作品をお待ちしております。
こちらのサイトの姉妹サイトで
簡単なTOPページの画像修正を
新規のSHIGOTOBAの案件として依頼中です。

もしご興味のある人がいましたらば
ぜひご参加のほどよろしくお願い致します。

http://www.shigotoba.example/task/view/472093
皆様、ご応募ありがとうございます。
これから選考に入らせていただきます。

このあと修正の可否などお伺いすることもあるかと思いますが
可能であればご返信いただければ幸いです。

1週間程度で最終的な採択をさせていただくつもりです。
それではよろしくお願い致します。

デザイン性が高く
ファーストビューで当事務所がお客様に伝えたいことを
的確に表現していただいた点

提案してくださいましたシゴトバーの皆様
多くの素晴らしいデザインを提案していただいてありがとうございました。
また今後もデザインを発注することがあると思いますので
その際はどうぞよろしくお願い致します。

```html
<!DOCTYPE html>
<html lang="ja">
<head>
<meta charset="utf-8">
<title>起業・独立サポート｜起業独立セミナー</title>
<link href="https://fonts.googleapis.com/css2?family=Noto+Sans+JP:wght@400;500;700;900&display=swap" rel="stylesheet">
<style>
:root{
  --navy:#1b3f7a;
  --blue:#2a6cc4;
  --sky:#bfe0f7;
  --sky-deep:#5aa8e0;
  --red:#d9322a;
  --orange:#f08a1c;
  --green:#5fb848;
  --teal:#3aa3d8;
  --gold:#f6c400;
  --ink:#333;
  --paper:#fff;
  --line:#d8dde4;
}
*{margin:0;padding:0;box-sizing:border-box}
html,body{width:695px;height:1200px;overflow:hidden;background:#eef1f4}
body{font-family:"Noto Sans JP",sans-serif;color:var(--ink);font-size:12px}
.page{width:695px;height:1200px;background:var(--paper);position:relative;overflow:hidden}
.topline{height:18px;background:#f4f6f8;border-bottom:1px solid var(--line);font-size:8px;color:#888;text-align:right;padding:4px 10px}
.header{height:52px;display:flex;align-items:center;padding:0 18px;gap:20px}
.brand{display:flex;flex-direction:column;line-height:1.15}
.brand small{font-size:9px;color:#555}
.brand b{font-size:19px;color:var(--navy);font-weight:700}
.tel{display:flex;align-items:center;gap:6px;font-size:20px;font-weight:700;color:var(--navy);margin-left:auto}
.contact{background:var(--navy);color:#fff;font-size:11px;padding:6px 14px;border-radius:3px;display:flex;align-items:center;gap:5px}
.nav{height:26px;display:flex;background:linear-gradient(#3c79c9,#1f5199)}
.nav a{flex:1;color:#fff;text-decoration:none;font-size:10.5px;text-align:center;line-height:26px;border-right:1px solid rgba(255,255,255,.35)}
.nav a:first-child{background:var(--navy)}
.hero{height:250px;position:relative;background:linear-gradient(180deg,#e6f3fc,var(--sky) 60%,#8cc4ec);overflow:hidden}
.hero-sub{position:absolute;left:190px;top:12px;font-size:16px;font-weight:700;color:var(--navy);background:rgba(255,255,255,.7);padding:2px 12px;border-radius:14px;z-index:2}
.hero-title{position:absolute;left:24px;top:34px;color:var(--navy);font-weight:900;font-size:48px;line-height:1.04;letter-spacing:2px;text-shadow:2px 2px 0 #fff;z-index:2}
.hero-title span{display:block;font-size:38px;letter-spacing:1px}
.price{position:absolute;left:24px;top:186px;background:var(--navy);color:#fff;padding:4px 10px;font-weight:700;font-size:12px;line-height:1.2;z-index:2}
.price em{font-style:normal;font-size:19px;color:var(--gold)}
.catch{position:absolute;left:170px;top:194px;background:var(--blue);color:#fff;font-weight:900;font-size:22px;padding:5px 18px;transform:skew(-8deg);border:2px solid #fff;z-index:2}
.catch b{color:var(--gold)}
.hero-photo{position:absolute;right:0;top:30px;width:260px;height:220px;background:linear-gradient(135deg,#f2f6fa,#c8dcef)}
.cta{display:block;width:360px;height:40px;margin:16px auto 0;background:linear-gradient(#f25a3a,var(--red));color:#fff;font-weight:900;font-size:22px;text-align:center;line-height:40px;border-radius:4px;box-shadow:0 3px 0 #9c1f18;text-decoration:none}
.cta-link{display:block;text-align:center;font-size:11px;color:var(--blue);margin-top:14px;text-decoration:underline}
.worries{width:575px;height:178px;margin:20px auto 0;border:2px solid var(--line);border-radius:6px;position:relative;padding:16px 24px}
.worries h2{display:inline-block;background:var(--red);color:#fff;font-size:19px;font-weight:900;padding:4px 18px;border-radius:4px;transform:skew(-6deg)}
.worries ul{list-style:none;margin-top:8px}
.worries li{display:flex;align-items:center;gap:8px;font-size:13px;font-weight:500;padding:6px 0;border-bottom:1px dashed var(--line);width:330px}
.worries li:last-child{border-bottom:none}
.worries-photo{position:absolute;right:20px;top:18px;width:170px;height:135px;background:linear-gradient(160deg,#f4f4f4,#d2d6dc)}
.solve-banner{margin:30px 0 0;height:40px;background:linear-gradient(#3c86d8,var(--navy));color:#fff;font-weight:900;font-size:22px;text-align:center;line-height:40px}
.solve-head{display:flex;align-items:center;gap:8px;padding:12px 0 8px;font-size:18px;font-weight:900;color:var(--navy);border-bottom:2px solid var(--navy);margin:0 40px}
.cards{display:grid;grid-template-columns:1fr 1fr;gap:14px;padding:14px 40px 0}
.card{border:1px solid var(--line);height:206px;display:flex;flex-direction:column}
.card h3{color:#fff;font-size:16px;font-weight:700;text-align:center;padding:14px 6px;line-height:1.3}
.card.green h3{background:var(--green)}
.card.blue h3{background:var(--teal)}
.card.orange h3{background:var(--orange)}
.card .body{padding:10px 14px;font-size:10.5px;line-height:1.6}
.card .lead{font-weight:700;font-size:12px;color:var(--navy);border-bottom:1px solid var(--line);margin-bottom:5px;padding-bottom:3px}
.card.orange .lead{color:var(--red)}
.card .ticks{list-style:none}
.card .ticks li::before{content:"□ ";color:var(--green)}
.card-photo{margin:0 14px 10px;flex:1;background:linear-gradient(135deg,#e9eef4,#c5d2e0)}
</style>
</head>
<body>
<div class="page">
  <div class="topline">起業をお考えの方へ、少人数制セミナーで基礎から実践まで丁寧にご案内します</div>
  <header class="header">
    <div class="brand"><small>森川会計事務所</small><b>起業・独立サポート</b></div>
    <div class="tel">
      <svg width="20" height="20" viewBox="0 0 24 24"><path fill="#1b3f7a" d="M6.6 10.8a15 15 0 0 0 6.6 6.6l2.2-2.2c.3-.3.7-.4 1-.2 1.1.4 2.3.6 3.6.6.6 0 1 .4 1 1V20c0 .6-.4 1-1 1A17 17 0 0 1 3 4c0-.6.4-1 1-1h3.5c.6 0 1 .4 1 1 0 1.3.2 2.5.6 3.6.1.3 0 .7-.2 1z"/></svg>
      03-5550-0182
    </div>
    <div class="contact">
      <svg width="12" height="10" viewBox="0 0 12 10"><rect x=".5" y=".5" width="11" height="9" fill="none" stroke="#fff"/><path d="M.5 .5 6 5.5 11.5 .5" fill="none" stroke="#fff"/></svg>
      お問合せ・ご相談
    </div>
  </header>
  <nav class="nav"><a href="#">起業セミナー</a><a href="#">講座内容</a><a href="#">講師紹介</a><a href="#">参加者の声</a><a href="#">よくあるご質問</a></nav>

  <section class="hero">
    <div class="hero-photo" role="img" aria-label="笑顔で手を差し出すビジネスウーマンの写真"></div>
    <p class="hero-sub">〜起業を志す方の学びの場、交流の場〜</p>
    <h1 class="hero-title">起業<br>独立<span>セミナー</span></h1>
    <div class="price">料金 <em>2,000円</em><br>定員 <em>10名まで</em></div>
    <div class="catch"><b>お手頃な価格</b>で、しっかり学べる!</div>
  </section>

  <a class="cta" href="#">今スグお申込み</a>
  <a class="cta-link" href="#">申込みフォームへ</a>

  <section class="worries">
    <h2>こんな悩みありませんか?</h2>
    <ul>
      <li><svg width="16" height="16" viewBox="0 0 16 16"><rect width="16" height="16" rx="3" fill="#d9322a"/><path d="M4 8l3 3 5-6" stroke="#fff" stroke-width="2" fill="none"/></svg>起業したいがまず何をはじめたらいいかわからない</li>
      <li><svg width="16" height="16" viewBox="0 0 16 16"><rect width="16" height="16" rx="3" fill="#d9322a"/><path d="M4 8l3 3 5-6" stroke="#fff" stroke-width="2" fill="none"/></svg>税金や銀行からの融資？起業について不安がある</li>
      <li><svg width="16" height="16" viewBox="0 0 16 16"><rect width="16" height="16" rx="3" fill="#d9322a"/><path d="M4 8l3 3 5-6" stroke="#fff" stroke-width="2" fill="none"/></svg>起業について相談する時間はほしい</li>
    </ul>
    <div class="worries-photo" role="img" aria-label="頭を抱えて悩むビジネスマンの写真"></div>
  </section>

  <div class="solve-banner">このセミナーで悩みを解決しませんか？</div>
  <h2 class="solve-head">
    <svg width="20" height="20" viewBox="0 0 20 20"><circle cx="10" cy="10" r="10" fill="#1b3f7a"/><rect x="9" y="4" width="2" height="2" fill="#fff"/><rect x="9" y="8" width="2" height="8" fill="#fff"/></svg>
    解決方法
  </h2>
  <div class="cards">
    <div class="card green">
      <h3>基礎から分かる<br>丁寧な講義</h3>
      <div class="body"><p class="lead">基礎の基礎から講義します</p>さらに税務面など必要な情報や知りたい事柄を具体的に丁寧に解説いたします。</div>
    </div>
    <div class="card blue">
      <h3>わからないところは<br>いつでも質問できる体制</h3>
      <div class="body"><p class="lead">少人数制</p>10名までの少人数制のため講師に直接質問することが可能です。その場で疑問を解消できます。</div>
    </div>
    <div class="card green">
      <h3>本当の起業ノウハウ</h3>
      <div class="body"><p class="lead">専門家による体験の講義内容</p>
        <ul class="ticks"><li>事業計画書の作り方</li><li>融資や助成金の基礎知識</li><li>税理士との付き合い方</li></ul>
        <p class="lead" style="margin-top:6px">100社以上の起業支援実績</p></div>
    </div>
    <div class="card orange">
      <h3>起業の仲間ができる</h3>
      <div class="body"><p class="lead">最大のメリットは</p>起業を志す仲間と出会えること。情報交換の輪が広がります。</div>
      <div class="card-photo" role="img" aria-label="セミナーで交流する参加者たちの写真"></div>
    </div>
  </div>
</div>
</body>
</html>
```